Candles

Need a good viable candle logo revamp and design for packaging and labels

Colors

Designer to choose colors to be used in the design.

Requirements
Must have
• Open to pretty much any designers ideas.
Nice to have
• We are an all natural soy based product

```html
<!DOCTYPE html>
<html lang="en">
<head>
<meta charset="utf-8">
<title>Marden Wicks – Label Designs</title>
<link rel="stylesheet" href="https://fonts.googleapis.com/css2?family=Saira:wght@700&family=Open+Sans:ital,wght@1,400&display=swap">
<style>
  :root {
    --page-bg: #ffffff;
    --rust-edge: #b24f2b;
    --rust-mid: #dd7a30;
    --orange: #f28322;
    --ink: #1d1d1d;
    --white: #ffffff;
    --map-on-rust: rgba(255, 255, 255, 0.10);
    --map-on-white: rgba(0, 0, 0, 0.045);
  }
  * { margin: 0; padding: 0; box-sizing: border-box; }
  html, body {
    width: 1200px;
    height: 876px;
    overflow: hidden;
    background: var(--page-bg);
  }
  .canvas {
    position: relative;
    width: 1200px;
    height: 876px;
  }
  .label {
    position: absolute;
    top: 288px;
    width: 432px;
    height: 300px;
    overflow: hidden;
    box-shadow: 0 10px 24px rgba(0, 0, 0, 0.18);
  }
  .label--rust {
    left: 163px;
    background: radial-gradient(ellipse at 55% 55%, var(--rust-mid) 0%, #cf6a2d 55%, var(--rust-edge) 100%);
  }
  .label--white {
    left: 603px;
    background: var(--white);
  }
  .label__map {
    position: absolute;
    inset: 0;
    z-index: 1;
  }
  .label--rust .label__map {
    background: radial-gradient(ellipse 48% 36% at 50% 48%, var(--map-on-rust) 0%, var(--map-on-rust) 55%, transparent 100%);
  }
  .label--white .label__map {
    background: radial-gradient(ellipse 48% 36% at 50% 48%, var(--map-on-white) 0%, var(--map-on-white) 55%, transparent 100%);
  }
  .label__frame {
    position: absolute;
    z-index: 2;
  }
  .label--rust .label__frame {
    inset: 14px 24px 16px 24px;
    border: 6px solid var(--white);
  }
  .label--white .label__frame {
    inset: 16px 26px 16px 26px;
    border: 6px solid var(--orange);
  }
  .label__content {
    position: absolute;
    inset: 0;
    z-index: 3;
    display: flex;
    flex-direction: column;
    align-items: center;
    padding-top: 52px;
  }
  .brand-circle {
    width: 114px;
    height: 114px;
    border-radius: 50%;
    border: 4px solid currentColor;
  }
  .label--rust .brand-circle { color: var(--white); }
  .label--white .brand-circle { color: var(--orange); }
  .brand-name {
    font-family: "Saira", "Arial Narrow", sans-serif;
    font-weight: 700;
    font-size: 44px;
    line-height: 1;
    margin-top: 6px;
    letter-spacing: -0.5px;
    white-space: nowrap;
  }
  .label--rust .brand-name { color: var(--white); }
  .label--white .brand-name { color: var(--ink); }
  .tagline {
    font-family: "Open Sans", Arial, sans-serif;
    font-style: italic;
    font-weight: 400;
    font-size: 17px;
    letter-spacing: 3.4px;
    margin-top: 6px;
    white-space: nowrap;
  }
  .label--rust .tagline { color: var(--white); }
  .label--white .tagline { color: var(--ink); }
</style>
</head>
<body>
<main class="canvas">
  <section class="label label--rust">
    <div class="label__map" role="img" aria-label="Faint dotted world map in the background"></div>
    <div class="label__frame"></div>
    <div class="label__content">
      <div class="brand-circle"></div>
      <h1 class="brand-name">Marden Wicks</h1>
      <p class="tagline">HAND POURED SOY CANDLES</p>
    </div>
  </section>

  <section class="label label--white">
    <div class="label__map" role="img" aria-label="Faint dotted world map in the background"></div>
    <div class="label__frame"></div>
    <div class="label__content">
      <div class="brand-circle"></div>
      <h2 class="brand-name">Marden Wicks</h2>
      <p class="tagline">HAND POURED SOY CANDLES</p>
    </div>
  </section>
</main>
</body>
</html>
```